Providing Back Office Solutions to Financial Advisors and Attorney Needs a Business Card Design

Need a Business Card Design that speaks to Financial Advisor and Attorneys. Some of the word that come to mind is Clean/Simple & Futuristic.

Industry/Entity Type

Business

```html
<!DOCTYPE html>
<html lang="en">
<head>
<meta charset="utf-8">
<title>Veridia Back Office Solutions – Business Card</title>
<link rel="stylesheet" href="https://fonts.googleapis.com/css2?family=Open+Sans:wght@400;700&display=swap">
<style>
  :root {
    --backdrop: #e9e6e2;
    --card: #ffffff;
    --brand: #1b63a8;
    --brand-deep: #12538f;
    --brand-light: #3f92d6;
    --text: #333333;
    --muted: #4a4a4a;
  }
  * { margin: 0; padding: 0; box-sizing: border-box; }
  html, body {
    width: 1200px; height: 1000px; overflow: hidden;
    background: var(--backdrop);
    font-family: "Open Sans", Arial, sans-serif;
  }
  .card {
    position: absolute; left: 266px; width: 666px; height: 397px;
    background: var(--card); border-radius: 24px;
    box-shadow: 0 2px 8px rgba(0,0,0,0.12);
  }
  .card--top { top: 74px; }
  .card--bottom { top: 533px; }

  .brand { position: absolute; left: 32px; top: 40px; display: flex; align-items: center; }
  .brand__square { width: 64px; height: 64px; background: var(--brand); }
  .brand__divider { width: 2px; height: 106px; background: var(--brand-deep); margin: 0 10px 0 14px; }
  .brand__name {
    font-size: 24px; font-weight: 700; color: var(--brand);
    line-height: 1.2; width: 220px;
  }

  .person { position: absolute; left: 32px; top: 184px; }
  .person__name { font-size: 20px; font-weight: 700; color: var(--brand-deep); letter-spacing: 0.2px; }
  .person__role { font-size: 15.5px; color: var(--muted); margin-top: 1px; }

  .address { position: absolute; left: 32px; top: 248px; font-size: 15.5px; color: var(--text); line-height: 23px; }

  .contacts { position: absolute; left: 32px; top: 303px; list-style: none; font-size: 15.5px; color: var(--text); }
  .contacts li { display: flex; align-items: center; height: 22.5px; }
  .contacts svg { width: 14px; height: 14px; margin-right: 8px; fill: var(--brand-deep); }

  .emblem { position: absolute; left: 388px; top: 36px; width: 240px; height: 324px; }
</style>
</head>
<body>

<section class="card card--top">
  <div class="brand">
    <div class="brand__square"></div>
    <div class="brand__divider"></div>
    <div class="brand__name">VERIDIA BACK OFFICE SOLUTIONS</div>
  </div>
  <div class="person">
    <div class="person__name">MARTIN HALE</div>
    <div class="person__role">Founder / CEO</div>
  </div>
  <div class="address">Level 18, 5 Meridian Tower<br>Lakeside, 14, North Coast</div>
  <ul class="contacts">
    <li><svg viewBox="0 0 16 16"><path d="M2 5c0-2 2-3 6-3s6 1 6 3v1h-3V5H5v1H2z M4 7h8l2 6H2z"/></svg>+0 000 000 000</li>
    <li><svg viewBox="0 0 16 16"><path d="M1 3h14v10H1z M1 3l7 6 7-6" stroke="#fff" stroke-width="1"/></svg>martin@veridiabackoffice.com</li>
    <li><svg viewBox="0 0 16 16"><circle cx="8" cy="8" r="7"/><path d="M1 8h14M8 1v14" stroke="#fff" stroke-width="1"/></svg>www.veridiabackoffice.com</li>
  </ul>
  <svg class="emblem" viewBox="0 0 240 324" role="img" aria-label="Brand emblem area">
    <defs>
      <linearGradient id="emblemFillA" x1="0" y1="0" x2="1" y2="1">
        <stop offset="0" stop-color="#3f92d6"/><stop offset="1" stop-color="#12538f"/>
      </linearGradient>
    </defs>
    <circle cx="120" cy="162" r="118" fill="url(#emblemFillA)"/>
  </svg>
</section>

<section class="card card--bottom">
  <div class="brand">
    <div class="brand__square"></div>
    <div class="brand__divider"></div>
    <div class="brand__name">VERIDIA BACK OFFICE SOLUTIONS</div>
  </div>
  <div class="person">
    <div class="person__name">MARTIN HALE</div>
    <div class="person__role">Founder / CEO</div>
  </div>
  <div class="address">Level 18, 5 Meridian Tower<br>Lakeside, 14, North Coast</div>
  <ul class="contacts">
    <li><svg viewBox="0 0 16 16"><path d="M2 5c0-2 2-3 6-3s6 1 6 3v1h-3V5H5v1H2z M4 7h8l2 6H2z"/></svg>+0 000 000 000</li>
    <li><svg viewBox="0 0 16 16"><path d="M1 3h14v10H1z M1 3l7 6 7-6" stroke="#fff" stroke-width="1"/></svg>martin@veridiabackoffice.com</li>
    <li><svg viewBox="0 0 16 16"><circle cx="8" cy="8" r="7"/><path d="M1 8h14M8 1v14" stroke="#fff" stroke-width="1"/></svg>www.veridiabackoffice.com</li>
  </ul>
  <svg class="emblem" viewBox="0 0 240 324" role="img" aria-label="Brand emblem area">
    <defs>
      <linearGradient id="emblemFillB" x1="0" y1="0" x2="1" y2="1">
        <stop offset="0" stop-color="#3f92d6"/><stop offset="1" stop-color="#12538f"/>
      </linearGradient>
    </defs>
    <circle cx="120" cy="162" r="118" fill="url(#emblemFillB)"/>
  </svg>
</section>

</body>
</html>
```